We are working with a new commercial flooring contractor in California. They work on schools, hospitals, and government projects.
A few websites for inspiration:
https://plainrockcoverings.com (These guys are competitors and provide the same work our client does).
https://tjtilework.com (Although NOT a contractor, the simplicity of this site is stunning).
https://www.quietlantern.com (NOT a flooring contractor, but this site is modern, and has a boldness to it).
https://www.sagemeadowatelier.com/en-us (website for an Architectural office that is clean and showcases their work. I can see this working for a flooring contractor).
Thank you for taking the time to consider designing a website for us. We are web developers based in Stockton, CA, USA. Most of our projects go through the same process. Understanding this process may help you win a project with us. We custom-code all of our websites in-house. We don’t have any requirements as to what tools you use for your design, but we ask that you follow these guidelines.
IMAGES:
If you use any images or icons in the design, we ask that you have a link to the asset so we can purchase the image/icon. Most of the designs we submit do not have the customer’s images on them unless they have some great images. Be creative; show us the feeling you are trying to portray with your image choices. Use any royalty-free site you choose. We subscribe to Kestral and mainly use their images, but we can purchase images outside of Kestral.
FONTS:
We ask that you identify the fonts you’re using in the design. This can be done in a message if you want. We typically use Vantor Fonts and Kestral Fonts.
CONTENT:
We're always open to different content and ideas. We often submit designs with stock images so the client can see our vision. We typically take pictures after the website launch to use their images with our vision. Lorem Ipsum is fine for paragraphs, but we ask that you make the Headers with correct English. We want to be able to show the vision and identify the sections of the website.
INSPIRATION:
We typically add a couple of links in the brief of websites we like to help you get started in your design.
REVISIONS:
We do not often ask for revisions of the designs unless we see something in the design that may not appeal to the client. If there are slight changes that we want to make, we do that in the development process.
FEEDBACK:
We rarely give feedback on designs during the design process. We are working on many website projects and do not have the time to provide feedback. We usually respond if your request is well thought out and asks specific questions, but a note asking “feedback, please” usually goes unanswered.

```html
<!DOCTYPE html>
<html lang="en">
<head>
<meta charset="UTF-8">
<title>Keelstone Flooring &amp; Construction</title>
<link href="https://fonts.googleapis.com/css2?family=Cormorant+Garamond:wght@500;600;700&family=Montserrat:wght@400;500;700&display=swap" rel="stylesheet">
<style>
:root{
  --red:#e35a52;
  --dark:#2f2f2f;
  --footer:#3a3a3a;
  --btn:#4b5150;
  --ink:#333;
  --muted:#555;
  --field:#f4f4f4;
  --line:#d9d9d9;
  --cream:#fbf4e8;
}
*{margin:0;padding:0;box-sizing:border-box}
html,body{width:1200px;height:4710px;overflow:hidden;background:#fff}
body{position:relative;font-family:'Montserrat',sans-serif;color:var(--ink)}
.abs{position:absolute}
h1,h2,h3{font-family:'Cormorant Garamond',serif;font-weight:600;letter-spacing:1px}
.btn{position:absolute;display:flex;align-items:center;justify-content:center;font-size:11.5px;font-weight:700;letter-spacing:1.6px;text-transform:uppercase;color:#fff;background:var(--btn)}
.btn.outline{background:transparent;border:2px solid #fff}
p.copy{font-size:12.5px;line-height:20px}

/* header */
.brand{left:119px;top:20px;display:flex;align-items:center;gap:10px}
.brand .mark{width:34px;height:34px;border-radius:50%;background:var(--red)}
.brand span{font-family:'Cormorant Garamond',serif;font-size:30px;font-weight:700;color:var(--dark)}
.lang{left:528px;top:44px;width:22px;height:22px;border-radius:50%;background:var(--red)}
.lang-caret{left:556px;top:50px;width:8px;height:8px;border-right:2px solid #555;border-bottom:2px solid #555;transform:rotate(45deg)}
.top-panel{left:589px;top:0;width:611px;height:653px;background:var(--dark)}
.main-nav{left:637px;top:48px;display:flex;gap:45px;font-size:11px;color:#fff;letter-spacing:.5px}
.hero-photo{left:368px;top:110px;width:748px;height:543px;background:linear-gradient(160deg,#f3f1ec 0%,#d9d5cc 45%,#b7885c 80%,#8e6a47 100%)}
.hero-title{left:124px;top:190px;font-size:68px;line-height:87px;color:var(--dark);font-weight:600}
.hero-text{left:124px;top:466px;width:225px;font-size:12px;line-height:20px;color:var(--ink)}
.hero-btn{left:393px;top:583px;width:229px;height:44px}

/* who we are */
.who-photo{left:0;top:755px;width:933px;height:511px;background:linear-gradient(180deg,#c7c8c6 0%,#a9b7bd 30%,#9fb0b7 70%,#6f7276 100%)}
.red-box{background:var(--red);color:#fff}
.who-box{left:514px;top:812px;width:551px;height:395px}
.who-box h2{position:absolute;left:56px;top:58px;font-size:54px}
.who-box p{position:absolute;left:56px;top:135px;width:420px;color:#fff}
.who-read{left:569px;top:1123px;width:163px;height:44px}
.who-loc{left:739px;top:1123px;width:227px;height:44px}

/* services */
.section-title{left:0;width:1200px;text-align:center;font-size:54px;color:var(--dark)}
.service-card{width:382px;height:291px;background:#fff;box-shadow:0 4px 14px rgba(0,0,0,.14);padding:38px 0 0 60px}
.service-card li{list-style:none;display:flex;align-items:center;gap:16px;font-size:11.5px;height:46px;color:var(--ink)}
.service-card li::before{content:"";width:14px;height:14px;border:3.5px solid var(--red);border-radius:50%}

/* slider */
.slider{left:0;top:1823px}
.slide-title{left:0;width:1200px;top:2322px;text-align:center;font-size:36px;color:var(--dark);font-weight:600}
.slide-text{left:295px;top:2392px;width:610px;text-align:center;font-size:12px;line-height:20px}

/* careers */
.careers-photo{left:0;top:2561px;width:993px;height:549px;background:linear-gradient(120deg,#3e4a4a 0%,#8d6c52 40%,#c9b59a 60%,#5c6b72 100%)}
.careers-box{left:529px;top:2879px;width:545px;height:357px}
.careers-box h2{position:absolute;left:47px;top:40px;font-size:54px}
.careers-box p{position:absolute;left:47px;top:120px;width:445px;color:#fff;font-size:12px}
.careers-btn{left:576px;top:3214px;width:227px;height:44px}

/* contact */
.contact-text{left:300px;top:3433px;width:600px;text-align:center;font-size:12px;line-height:20px}
.field{left:287px;width:624px;background:var(--field);border:1px solid var(--line);font-size:11.5px;color:#aaa;text-align:center;padding-top:17px}
.field.msg{padding-top:20px}

/* footer */
.site-footer{left:24px;top:4044px;width:1150px;height:593px;background:var(--footer);color:#fff}
.footer-brand{left:500px;top:88px;width:158px;height:158px;border-radius:50%;background:var(--cream);display:flex;align-items:center;justify-content:center;font-family:'Cormorant Garamond',serif;font-weight:700;font-size:32px;color:var(--dark)}
.footer-text{left:275px;top:280px;width:600px;text-align:center;font-size:12px;line-height:20px}
.footer-nav{left:100px;top:357px;width:950px;height:58px;border-top:1px solid #aaa;border-bottom:1px solid #aaa}
.footer-nav a{position:absolute;top:21px;font-size:12px;color:#fff;text-decoration:none}
.social{top:465px;width:40px;height:40px;border-radius:50%}
.copyright{left:0;top:4667px;width:1200px;text-align:center;font-size:11.5px;color:var(--ink)}
</style>
</head>
<body>

<!-- Header -->
<div class="abs top-panel"></div>
<div class="abs brand"><div class="mark"></div><span>Keelstone</span></div>
<div class="abs lang" role="img" aria-label="Language selector"></div>
<div class="abs lang-caret"></div>
<nav class="abs main-nav"><span>HOME</span><span>ABOUT</span><span>SERVICES</span><span>CAREERS</span><span>CONTACT US</span></nav>

<div class="abs hero-photo" role="img" aria-label="Bright modern home interior with staircase, kitchen island and wood flooring"></div>
<h1 class="abs hero-title">MAKING HOUSES<br>FEEL LIKE<br>A HOME</h1>
<p class="abs hero-text">Lorem Ipsum is simply dummy text of the printing and typesetting industry. Lorem Ipsum has been the industry's standard dummy text.Lorem Ipsum is simply dummy text of the printing and typesetting industry.</p>
<a class="btn hero-btn">Get Appointment</a>

<!-- Who we are -->
<div class="abs who-photo" role="img" aria-label="Empty modern room with concrete ceiling, glass wall, potted plant and grey carpet tile"></div>
<section class="abs red-box who-box">
  <h2>WHO WE ARE</h2>
  <p class="copy">Lorem Ipsum is simply dummy text of the printing and typesetting industry. Lorem Ipsum has been the industry's standard dummy text.Lorem Ipsum is simply dummy text of the printing and typesetting industry. Lorem Ipsum has been the industry's standard dummy text.Lorem Ipsum is simply dummy text of the printing and typesetting industry.</p>
</section>
<a class="btn who-read">Read More</a>
<a class="btn outline who-loc">View Our Location</a>

<!-- Services -->
<h2 class="abs section-title" style="top:1355px">OUR SERVICES</h2>
<ul class="abs service-card" style="left:207px;top:1474px">
  <li>Bondability Up to 20 Million</li>
  <li>Experience Modification Rate .60 – .64</li>
  <li>Installers Certified for Secure Entities</li>
  <li>Overnight &amp; Weekend Work Capacity</li>
  <li>Design/Build Expertise</li>
</ul>
<ul class="abs service-card" style="left:611px;top:1474px;padding-left:58px">
  <li>Value-Engineering Analysis</li>
  <li>Specification &amp; Budgeting Assistance</li>
  <li>Supplier Negotiations &amp; Scaled Pricing</li>
  <li>Material Warehousing for Ongoing Jobs</li>
</ul>

<!-- Slider -->
<svg class="abs slider" width="1200" height="527" viewBox="0 0 1200 527">
  <defs>
    <linearGradient id="tileL" x1="0" y1="0" x2="1" y2="1"><stop offset="0" stop-color="#6f7375"/><stop offset="1" stop-color="#d4d6d6"/></linearGradient>
    <linearGradient id="tileR" x1="0" y1="0" x2="0" y2="1"><stop offset="0" stop-color="#8e9090"/><stop offset=".7" stop-color="#c9c6c1"/><stop offset="1" stop-color="#b58c64"/></linearGradient>
    <linearGradient id="tileC" x1="0" y1="0" x2="1" y2="0"><stop offset="0" stop-color="#e7e3dc"/><stop offset="1" stop-color="#c9744a"/></linearGradient>
  </defs>
  <rect x="0" y="0" width="256" height="527" fill="url(#tileL)" role="img" aria-label="Bathroom with hexagon patterned tile"/>
  <rect x="944" y="0" width="256" height="527" fill="url(#tileR)" role="img" aria-label="Room with wood floor and a stepladder"/>
  <path d="M0,0 L1200,0 Q600,120 0,0 Z" fill="#fff"/>
  <path d="M0,527 L1200,527 Q600,407 0,527 Z" fill="#fff"/>
  <rect x="256" y="0" width="20" height="527" fill="#fff"/>
  <rect x="924" y="0" width="20" height="527" fill="#fff"/>
  <rect x="276" y="61" width="648" height="408" fill="url(#tileC)" role="img" aria-label="Flooring installation scene with laptop video preview"/>
  <rect x="345" y="76" width="505" height="325" rx="6" fill="#f2f2f2"/>
  <rect x="370" y="100" width="460" height="285" fill="#3c3c3c" role="img" aria-label="Video still of a dark bathroom with freestanding tub"/>
  <circle cx="600" cy="262" r="31" fill="none" stroke="#fff" stroke-width="4"/>
  <path d="M592,247 L614,262 L592,277 Z" fill="#fff"/>
  <circle cx="260" cy="264" r="27" fill="var(--red)"/>
  <path d="M265,254 L255,264 L265,274" fill="none" stroke="#fff" stroke-width="4"/>
  <circle cx="939" cy="264" r="27" fill="var(--red)"/>
  <path d="M934,254 L944,264 L934,274" fill="none" stroke="#fff" stroke-width="4"/>
</svg>
<h3 class="abs slide-title">TILE</h3>
<p class="abs slide-text">Lorem Ipsum is simply dummy text of the printing and typesetting industry. Lorem Ipsum has been the industry's standard dummy text ever since the 1500s, when an unknown printer took a galley of type and scrambled it to make a type specimen book. It has survived not only five centuries, but also the leap into electronic typesetting, remaining essentially unchanged.</p>

<!-- Careers -->
<div class="abs careers-photo" role="img" aria-label="Team of colleagues meeting around a table"></div>
<section class="abs red-box careers-box">
  <h2>CAREERS</h2>
  <p class="copy">Lorem Ipsum is simply dummy text of the printing and typesetting industry. Lorem Ipsum has been the industry's standard dummy text ever since the 1500s, when an unknown printer took a galley of type and scrambled it to make a type specimen book. It has survived not only five centuries, but also the leap into electronic typesetting, remaining essentially unchanged.Lorem Ipsum is simply dummy text of the printing and typesetting industry. Lorem Ipsum has been the industry's standard dummy text ever since the 1500s,</p>
</section>
<a class="btn careers-btn">Apply Now</a>

<!-- Contact -->
<h2 class="abs section-title" style="top:3340px">CONTACT US</h2>
<p class="abs contact-text">Lorem Ipsum is simply dummy text of the printing and typesetting industry. Lorem Ipsum has been the industry's standard dummy text ever since the 1500s,</p>
<div class="abs field" style="top:3510px;height:50px">Name</div>
<div class="abs field" style="top:3572px;height:50px">Email</div>
<div class="abs field" style="top:3635px;height:50px">Subject</div>
<div class="abs field msg" style="top:3698px;height:242px">Message</div>

<!-- Footer -->
<footer class="abs site-footer">
  <div class="abs footer-brand">Keelstone</div>
  <p class="abs footer-text">Lorem Ipsum is simply dummy text of the printing and typesetting industry. Lorem Ipsum has been the industry's standard dummy text ever since the 1500s,</p>
  <nav class="abs footer-nav">
    <a style="left:165px">HOME</a>
    <a style="left:299px">ABOUT</a>
    <a style="left:445px">SERVICES</a>
    <a style="left:598px">CAREERS</a>
    <a style="left:763px">CONTACT US</a>
  </nav>
  <div class="abs social" style="left:501px;background:#2f7fe8" role="img" aria-label="Social profile link"></div>
  <div class="abs social" style="left:556px;background:#d8508a" role="img" aria-label="Social profile link"></div>
  <div class="abs social" style="left:609px;background:#3a9be8" role="img" aria-label="Social profile link"></div>
</footer>
<p class="abs copyright">Copyright © 2023 Keelstone. All rights reserved.</p>

</body>
</html>
```